New Business Card Design Project

possibly double-sided card, with one side in color. leaves, a tree branch, or a tree of life, like laurel, olive, pine ... or a seed that grows. visual discreet and stylized or naive. no photo. no human silhouette Modern Typo possibly rounded corners matte paper, no selective varnish, neither gold nor silver English brief Double sided business card, with eventually a single colored side. Leaves, a tree branch or a tree of life, laurel, olive tree, pine tree ... or a growing seed. The design has to be discreet and stylized or naive. No human silhouettes Modern made Possibly rounded corners Matte paper, no selective varnish, no gold, no silver
Updates

I really prefer toned or subtles tones, Bluish / greenwich gray, verdigris ... Elegant and discreet colors Write "HUMANISTIC HYPNOTHERAPY, SYMBOLIC THERAPY" on 2 lines and on One side only (not with the name and address) Not use pictogram (such , address...)

Contact Information for Business Card

Hypnothérapie humaniste
Thérapie symbolique

Mireille Fontanel
Hypnothérapeute
06 48 17 35 82
84 rue des Glycines, 33990 Valbrume-sur-Lande
therapie.fontanel@exemplemail.fr

Colors
33b8a4
3176b5

Requirements
Must have
• sober, elegant and refined card Sober design, elegant, plain
Nice to have
• desired colors: gray, blue-gis, greyish, khaki ... Desired colors: gray, blue-gray, grayish green, khaki, ...
Should not have
• gaudy colors, bright greens no bright gold neon colors

```html
<!DOCTYPE html>
<html lang="fr">
<head>
<meta charset="UTF-8">
<title>Mireille Fontanel — Carte de visite</title>
<link rel="stylesheet" href="https://fonts.googleapis.com/css2?family=Quicksand:wght@300;400;500&display=swap">
<style>
  :root {
    --page: #ffffff;
    --stage: #f5fafd;
    --card: #7fc6d7;
    --ink: #ffffff;
    --shadow: rgba(60, 80, 90, 0.18);
  }
  * { margin: 0; padding: 0; box-sizing: border-box; }
  html, body {
    width: 1200px;
    height: 1200px;
    overflow: hidden;
    background: var(--page);
  }
  .stage {
    position: absolute;
    left: 110px;
    top: 0;
    width: 994px;
    height: 1200px;
    background: var(--stage);
  }
  .card {
    position: absolute;
    width: 717px;
    height: 410px;
    border-radius: 32px;
    background: var(--card);
    box-shadow: 10px 12px 18px var(--shadow);
    color: var(--ink);
    font-family: "Quicksand", sans-serif;
    text-align: center;
  }
  .card--front { left: 238px; top: 141px; }
  .card--back { left: 244px; top: 654px; }

  .block { position: absolute; left: 0; width: 100%; line-height: 1; white-space: nowrap; }

  .practice {
    top: 181px;
    font-size: 23px;
    font-weight: 500;
    letter-spacing: 0.3em;
    padding-left: 0.3em;
  }
  .practice-sub {
    top: 211px;
    font-size: 20px;
    font-weight: 500;
    letter-spacing: 0.29em;
    padding-left: 0.29em;
  }
  .rule {
    position: absolute;
    left: 292px;
    width: 147px;
    height: 3px;
    background: var(--ink);
  }
  .card--front .rule { top: 332px; }
  .card--back .rule { top: 206px; left: 286px; }

  .name {
    top: 98px;
    font-size: 44px;
    font-weight: 400;
    letter-spacing: 0.04em;
  }
  .title {
    top: 148px;
    font-size: 18px;
    font-weight: 400;
    letter-spacing: 0.4em;
    padding-left: 0.4em;
  }
  .contact {
    top: 251px;
    font-size: 18px;
    font-weight: 400;
    letter-spacing: 0.05em;
    line-height: 29px;
    font-style: normal;
  }
</style>
</head>
<body>
  <div class="stage"></div>

  <section class="card card--front">
    <p class="block practice">HYPNOTHÉRAPIE HUMANISTE</p>
    <p class="block practice-sub">THÉRAPIE SYMBOLIQUE</p>
    <div class="rule"></div>
  </section>

  <section class="card card--back">
    <h1 class="block name">Mireille Fontanel</h1>
    <p class="block title">HYPNOTHÉRAPEUTE</p>
    <div class="rule"></div>
    <address class="block contact">
      06 48 17 35 82<br>
      84 rue des Glycines, 33990 Valbrume-sur-Lande<br>
      therapie.fontanel@exemplemail.fr
    </address>
  </section>
</body>
</html>
```